Modern Business Card for Lanternfield 2018

Our company assumes the best about people. We are creating an online community of entrepreneurs and business leaders who struggle with marketing their business online.

This business card should POP! We recently got a new logo and are launching a new website next month, so our business cards should make a statement that feels:
-Fresh
-Smart
-Trustworthy
-Fun

Target Market(s)

small business owners, entrepreneurs

Industry/Entity Type

Digital Marketing

Contact Information for Business Card

Dimensions: 3.5" x 2"

Font styles to use
Sans Serif

Colors
f37122
ffffff

Requirements
Must have
• We need a business card with a modern, bold design. We will use one side of the card as a lead-generation offer, so text on one side will need to fit up to 140 characters. The business card should stick to our core colors (orange, black, and white).
Nice to have
• We think a vertical "portrait" design could be interesting.
Should not have
• Should not look like a traditional business card. The round icon should stand out from a distance.

```html
<!DOCTYPE html>
<html lang="en">
<head>
<meta charset="utf-8">
<title>Lanternfield Business Card</title>
<link rel="stylesheet" href="https://fonts.googleapis.com/css2?family=Open+Sans:wght@400;600;700;800&display=swap">
<style>
  :root {
    --orange: #f37122;
    --white: #ffffff;
    --black: #1b1b1b;
    --panel-grey: #e6e6e6;
    --rule-grey: #6b6b6b;
    --backdrop: #ecebe8;
  }
  * { box-sizing: border-box; margin: 0; padding: 0; }
  html, body {
    width: 1200px; height: 960px; overflow: hidden;
    background: var(--backdrop);
    font-family: "Open Sans", Arial, sans-serif;
  }
  .card {
    position: absolute; left: 250px;
    width: 700px; height: 400px;
    overflow: hidden;
    box-shadow: 0 10px 28px rgba(0,0,0,0.18);
  }

  /* Back: lead-generation offer */
  .card-back { top: 50px; background: var(--orange); color: var(--white); }
  .card-back .brand {
    position: absolute; left: 40px; top: 70px; width: 250px;
    display: flex; flex-direction: column; align-items: center; gap: 14px;
  }
  .card-back .brand-dot {
    width: 110px; height: 110px; border-radius: 50%; background: var(--white);
  }
  .card-back .brand-name {
    font-weight: 700; font-size: 30px; color: var(--white);
  }
  .card-back .divider {
    position: absolute; left: 318px; top: 36px; width: 1px; height: 190px;
    background: rgba(255,255,255,0.55);
  }
  .offer { position: absolute; left: 350px; top: 36px; width: 320px; }
  .offer-headline {
    font-weight: 800; font-size: 21px; line-height: 1.08; text-transform: uppercase;
  }
  .offer-body { margin-top: 8px; font-size: 17px; line-height: 1.2; font-weight: 400; }
  .offer-url { margin-top: 10px; font-size: 19px; font-weight: 700; }
  .notes-panel {
    position: absolute; left: 36px; right: 36px; bottom: 30px; height: 112px;
    background: var(--panel-grey); border-radius: 18px;
    padding: 32px 36px 0;
  }
  .notes-line { height: 1px; background: var(--rule-grey); margin-bottom: 34px; }

  /* Front: contact side */
  .card-front { top: 500px; background: var(--white); }
  .card-front .edge-tab {
    position: absolute; left: 0; top: 40px; width: 14px; height: 110px; background: var(--black);
  }
  .card-front .brand {
    position: absolute; left: 70px; top: 60px;
    display: flex; flex-direction: column; align-items: center; gap: 12px;
  }
  .card-front .brand-dot {
    width: 120px; height: 120px; border-radius: 50%; background: var(--orange);
  }
  .card-front .brand-name { font-weight: 700; font-size: 26px; color: var(--orange); }
  .contact-band {
    position: absolute; left: 320px; right: 0; top: 150px; height: 150px;
    background: var(--orange); color: var(--white);
    padding: 26px 30px;
  }
  .contact-name { font-weight: 800; font-size: 26px; text-transform: uppercase; line-height: 1.1; }
  .contact-title { font-weight: 700; font-size: 20px; text-transform: uppercase; line-height: 1.2; }
  .contact-email { font-size: 19px; font-weight: 400; margin-top: 4px; }
</style>
</head>
<body>
  <section class="card card-back" aria-label="Card back: offer">
    <div class="brand">
      <span class="brand-dot"></span>
      <span class="brand-name">Lanternfield</span>
    </div>
    <div class="divider"></div>
    <div class="offer">
      <p class="offer-headline">Reach more people.<br>Make more money.<br>Create more impact.</p>
      <p class="offer-body">Get your free Lanternfield Starter Package and our marketing guide today at</p>
      <p class="offer-url">Lanternfieldnow.com/start</p>
    </div>
    <div class="notes-panel">
      <div class="notes-line"></div>
      <div class="notes-line"></div>
    </div>
  </section>

  <section class="card card-front" aria-label="Card front: contact">
    <div class="edge-tab"></div>
    <div class="brand">
      <span class="brand-dot"></span>
      <span class="brand-name">Lanternfield</span>
    </div>
    <div class="contact-band">
      <p class="contact-name">Mark Delaney</p>
      <p class="contact-title">Story Marketing Coach</p>
      <p class="contact-email">mark@lanternfieldnow.com</p>
    </div>
  </section>
</body>
</html>
```